Marrunga Gymkhana community event

We are looking for a bright new poster for our annual gymkhana event. We are a remote outback town in the Flinders Ranges, South Australia with a very small population (27 people)
Our picnic gymkhana is a community even bringing families amd their ponies from 100 of kms away for a fun filled day.
We have events for junior and senior riders events for spectators and generally lots of fun. Our poster should include our sponsor list, information like live evening entertainment, catering and bar facilities. The event is October 15th 2022.
I have photos etc if you need them will upload them as needed.
Poster should be easy to read and eye catching.

Target Market(s)

Local community

Industry/Entity Type

Horse and family event

Requirements
Must have
• Title sponsor list dates and general information
Nice to have
• Colours

```html
<!DOCTYPE html>
<html lang="en">
<head>
<meta charset="utf-8">
<title>Marrunga Gymkhana Poster</title>
<link rel="stylesheet" href="https://fonts.googleapis.com/css2?family=Rye&family=Poppins:wght@400;500;600;700;800&family=Oswald:wght@300;400;500&display=swap">
<style>
  :root{
    --page:#e3e3e3;
    --dark:#3b2f27;
    --dark-deep:#2f251f;
    --tan:#a88d68;
    --tan-light:#c2a67e;
    --gold:#c9a877;
    --white:#ffffff;
    --ink:#2e241d;
    --rule:#efe6d8;
  }
  *{margin:0;padding:0;box-sizing:border-box}
  html,body{width:1200px;height:2400px;overflow:hidden;background:var(--page)}
  .poster{
    position:absolute;left:40px;top:360px;width:1120px;height:1680px;overflow:hidden;
    background:linear-gradient(180deg,var(--dark-deep) 0%,var(--dark) 30%,#4a3b2f 40%,var(--tan) 47%,#b39672 62%,#a08363 78%,#8f7356 92%);
    box-shadow:0 6px 18px rgba(0,0,0,.35);
    font-family:"Poppins",sans-serif;color:var(--white);
  }
  .photo{position:absolute}
  .photo--riders-left{left:6px;top:302px;width:376px;height:396px;border-radius:40% 50% 10% 30%;
    background:radial-gradient(ellipse at 55% 55%,#8a4a34 0%,#6b4a3a 45%,rgba(59,47,39,0) 75%)}
  .photo--rider-right{left:852px;top:315px;width:268px;height:531px;border-radius:45% 10% 20% 40%;
    background:radial-gradient(ellipse at 50% 55%,#9a5836 0%,#7a4a32 45%,rgba(59,47,39,0) 78%)}
  .photo--rider-middle{left:618px;top:587px;width:321px;height:283px;border-radius:50%;
    background:radial-gradient(ellipse at 50% 50%,#7d4529 0%,#5c3e2e 45%,rgba(120,90,60,0) 75%)}
  .title{position:absolute;left:0;width:1120px;text-align:center;font-family:"Rye",serif;font-weight:400;
    color:var(--gold);letter-spacing:1px;line-height:1;
    text-shadow:-3px -3px 0 var(--dark-deep),3px -3px 0 var(--dark-deep),-3px 3px 0 var(--dark-deep),3px 3px 0 var(--dark-deep),0 3px 0 var(--dark-deep),0 -3px 0 var(--dark-deep),3px 0 0 var(--dark-deep),-3px 0 0 var(--dark-deep)}
  .title--top{top:84px;font-size:112px}
  .title--bottom{top:222px;font-size:100px}
  .tagline{position:absolute;left:0;width:1120px;top:372px;text-align:center;font-weight:500;
    font-size:29px;line-height:37px;letter-spacing:.5px}
  .date{position:absolute;left:337px;top:519px;width:488px;height:59px;border:2px solid var(--tan-light);
    display:flex;font-weight:500;font-size:44px;line-height:55px}
  .date__day{background:var(--tan-light);color:var(--ink);padding:0 10px 0 12px}
  .date__year{background:var(--dark);color:var(--tan-light);flex:1;text-align:center}
  .food{position:absolute;left:68px;font-family:"Oswald",sans-serif;text-transform:uppercase;line-height:1}
  .food--bar{top:756px;font-size:52px;font-weight:300;color:var(--white);letter-spacing:-1px}
  .food--dinner{top:816px;font-size:68px;font-weight:400;color:var(--ink);letter-spacing:-1.5px}
  .snap{position:absolute;background:var(--white);padding:12px 12px 30px;box-shadow:0 4px 10px rgba(0,0,0,.35)}
  .snap__img{width:100%;height:100%}
  .snap__pin{position:absolute;top:-14px;left:50%;width:16px;height:16px;border-radius:50%;background:#d3232b;margin-left:-8px}
  .snap--one{left:-6px;top:915px;width:200px;height:236px;transform:rotate(4deg)}
  .snap--two{left:190px;top:915px;width:222px;height:240px;transform:rotate(-9deg)}
  .snap--three{left:672px;top:838px;width:258px;height:282px;transform:rotate(5deg)}
  .snap--four{left:930px;top:830px;width:210px;height:250px;transform:rotate(-7deg)}
  .snap--one .snap__img{background:linear-gradient(180deg,#6d8fc0 0%,#8a7a6a 45%,#b29a7a 100%)}
  .snap--two .snap__img{background:linear-gradient(180deg,#a8927a 0%,#3d5a9e 55%,#8b5a3c 100%)}
  .snap--three .snap__img{background:linear-gradient(180deg,#8fb4e0 0%,#b9b6b0 45%,#4a4f66 100%)}
  .snap--four .snap__img{background:linear-gradient(180deg,#2a2a30 0%,#4a4550 55%,#7a3a5a 100%)}
  .badge{position:absolute;left:425px;top:907px;width:248px;height:248px}
  .badge__text{position:absolute;left:425px;top:907px;width:248px;height:248px;text-align:center;color:var(--tan-light)}
  .badge__price{position:absolute;top:36px;width:100%;font-family:"Oswald",sans-serif;font-weight:500;font-size:100px;line-height:1;color:var(--white)}
  .badge__price sup{font-size:44px;vertical-align:top;position:relative;top:6px}
  .badge__label{position:absolute;top:146px;width:100%;font-weight:700;font-size:25px;line-height:30px}
  .badge__note{position:absolute;top:178px;width:100%;font-size:12px;color:var(--white)}
  .horse-box{position:absolute;left:65px;top:1247px;width:373px;height:149px;border:2px solid #e8dccb;border-left:none;border-bottom-right-radius:8px;border-top-right-radius:8px}
  .horse-tab{position:absolute;left:65px;top:1214px;height:62px;padding:0 16px;background:var(--dark);border-radius:8px;
    font-weight:700;font-size:36px;line-height:62px}
  .horse-info{position:absolute;left:65px;top:1286px;font-size:19px;line-height:28px;color:var(--ink)}
  .horse-info b{font-weight:600}
  .slider{position:absolute;left:65px;top:1390px;width:62px;height:12px;border-radius:6px;background:#e8dccb}
  .cause{position:absolute;left:65px;top:1414px;font-weight:500;font-size:27px;color:var(--ink)}
  .no-byo{position:absolute;left:65px;top:1444px;font-weight:800;font-size:42px;color:var(--white);line-height:1.1}
  .thanks{position:absolute;left:0;width:1120px;top:1497px;text-align:center;font-weight:500;font-size:16.5px;color:var(--ink)}
  .nonhorse-tab{position:absolute;left:626px;top:1195px;width:428px;height:61px;background:var(--white);border-radius:6px;
    color:var(--ink);font-weight:700;font-size:35px;line-height:61px;text-align:center}
  .nominations{position:absolute;left:626px;top:1270px;display:flex;align-items:center;color:var(--ink)}
  .nominations__price{font-family:"Oswald",sans-serif;font-weight:500;font-size:56px;line-height:1;color:var(--white);margin-right:14px}
  .nominations__price sup{font-size:26px;vertical-align:top}
  .nominations__text{font-weight:700;font-size:25px;line-height:26px;color:var(--dark)}
  .contact-head{position:absolute;left:624px;top:1339px;font-weight:700;font-size:32px;line-height:40px;color:var(--ink)}
  .rule{position:absolute;left:626px;width:448px;height:2px;background:var(--rule)}
  .contact{position:absolute;left:628px;font-weight:600;font-size:18px;line-height:21px;color:var(--dark)}
  .contact span{color:var(--white)}
  .disclaimer{position:absolute;left:626px;top:1431px;font-size:19px;line-height:26px;color:var(--ink)}
  .sponsor-band{position:absolute;left:0;top:1536px;width:1120px;height:144px}
  .sponsor-label{position:absolute;left:82px;top:1607px;font-weight:500;font-size:17px;color:var(--ink)}
</style>
</head>
<body>
<main class="poster">
  <div class="photo photo--riders-left" role="img" aria-label="Photo of two riders on horseback at full gallop"></div>
  <div class="photo photo--rider-right" role="img" aria-label="Photo of a young rider in a pink vest on a chestnut horse"></div>
  <div class="photo photo--rider-middle" role="img" aria-label="Photo of a rider cantering on a bay horse"></div>

  <h1 class="title title--top">MARRUNGA</h1>
  <h1 class="title title--bottom">GYMKHANA</h1>

  <p class="tagline">COME AND JOIN US AT<br>ONE OF SOUTH AUSTRALIA`S<br>LONGEST RUNNING PICNIC RACES!</p>

  <div class="date"><span class="date__day">OCTOBER 15TH</span><span class="date__year">2022</span></div>

  <p class="food food--bar">Food &amp; Bar Facilities All Day</p>
  <p class="food food--dinner">Roasts &amp; Rib Dinner</p>

  <div class="snap snap--one"><span class="snap__pin"></span><div class="snap__img" role="img" aria-label="Photo of a barrel event in the arena"></div></div>
  <div class="snap snap--two"><span class="snap__pin"></span><div class="snap__img" role="img" aria-label="Photo of a child holding a trophy"></div></div>
  <div class="snap snap--three"><span class="snap__pin"></span><div class="snap__img" role="img" aria-label="Photo of spectators in hats chatting"></div></div>
  <div class="snap snap--four"><span class="snap__pin"></span><div class="snap__img" role="img" aria-label="Photo of evening dancing under lights"></div></div>

  <svg class="badge" viewBox="0 0 248 248" aria-hidden="true">
    <circle cx="124" cy="124" r="108" fill="#3b2f27"/>
    <circle cx="124" cy="124" r="112" fill="none" stroke="#3b2f27" stroke-width="16" stroke-dasharray="7 7"/>
    <circle cx="124" cy="124" r="100" fill="none" stroke="#e8dccb" stroke-width="2"/>
  </svg>
  <div class="badge__text">
    <div class="badge__price"><sup>$</sup>15</div>
    <div class="badge__label">ADMISSION</div>
    <div class="badge__note">*CHILDREN U/15 FREE</div>
  </div>

  <div class="horse-box"></div>
  <div class="horse-tab">HORSE EVENTS</div>
  <p class="horse-info">GYMKHANA EVENT NOMINATIONS-<br>Junior - <b><sup>$</sup>20.00</b> &nbsp;Senior - <b><sup>$</sup>30.00</b><br>For the day(per horse).</p>
  <div class="slider"></div>
  <p class="cause">HELP SUPPORT THE CAUSE</p>
  <p class="no-byo">NO BYO ALCOHOL</p>

  <div class="nonhorse-tab">NON-HORSE EVENTS</div>
  <div class="nominations">
    <div class="nominations__price"><sup>$</sup>2</div>
    <div class="nominations__text">ALL NOMINATIONS<br>PER PERSON PER EVENT</div>
  </div>
  <p class="contact-head">FOR MORE INFO CONTACT</p>
  <div class="rule" style="top:1380px"></div>
  <p class="contact" style="top:1384px">JESS HARTLEY - <span>8612 3907</span></p>
  <p class="contact" style="top:1404px">EMAIL - <span>jesshartley.events@mail.com</span></p>
  <div class="rule" style="top:1428px"></div>
  <p class="disclaimer">*All riders ride at their own risk.<br>&nbsp;&nbsp;Dogs must be on leash at all times.</p>

  <p class="thanks">*THE GYMKHANA COMMITTEE WISHES TO THANK ALL SPONSERS AND DONORS FOR THEIR GENEROUS SUPPORT*</p>

  <svg class="sponsor-band" viewBox="0 0 1120 144" preserveAspectRatio="none" aria-hidden="true">
    <path fill="#3b2f27" d="M0,8 L60,4 L120,12 L180,6 L240,14 L300,8 L360,16 L420,6 L480,12 L540,4 L600,14 L660,8 L720,16 L780,6 L840,12 L900,4 L960,14 L1020,8 L1080,12 L1120,6 L1120,144 L0,144 Z"/>
    <path fill="#dcdcdc" d="M0,20 L40,26 L90,18 L150,28 L210,20 L270,30 L330,22 L390,30 L450,20 L510,28 L570,22 L630,32 L690,22 L750,30 L810,20 L870,28 L930,22 L990,30 L1050,22 L1120,28 L1120,144 L0,144 Z"/>
  </svg>
  <p class="sponsor-label">OUR SPONSERS</p>
</main>
</body>
</html>
```